DOVVRANTI Label and bottle design

We have already provided attached an idea concept of a label and bottle shape example, we now require designers to take this basic concept and advance it to the final label design using your own design creativity.
Please see attached the full product brief

```html
<!DOCTYPE html>
<html lang="en">
<head>
<meta charset="utf-8">
<title>DOVVRANTI Ink Vanti Label</title>
<link href="https://fonts.googleapis.com/css2?family=Montserrat:wght@500;600;800;900&display=swap" rel="stylesheet">
<style>
  :root {
    --page-bg: #f2f2f2;
    --label-dark: #2e2f2f;
    --brand-yellow: #f3ec2c;
    --accent-yellow: #ece33a;
    --text-light: #ffffff;
    --text-soft: #e6e6e6;
  }
  * { margin: 0; padding: 0; box-sizing: border-box; }
  html, body {
    width: 1200px;
    height: 1200px;
    overflow: hidden;
    background: var(--page-bg);
  }
  .canvas {
    width: 1200px;
    height: 1200px;
    display: flex;
    align-items: center;
    justify-content: center;
  }
  .label {
    position: relative;
    width: 700px;
    height: 1000px;
    background: var(--label-dark);
    overflow: hidden;
    font-family: "Montserrat", sans-serif;
    color: var(--text-light);
  }
  .accent-area {
    position: absolute;
    left: 0;
    right: 0;
    bottom: 0;
    height: 220px;
    background: radial-gradient(circle at 0% 100%, var(--accent-yellow) 0%, var(--label-dark) 50%);
  }
  .brand-name {
    position: absolute;
    top: 95px;
    left: 0;
    right: 0;
    text-align: center;
    font-weight: 900;
    font-size: 74px;
    letter-spacing: 1px;
    line-height: 1;
    color: var(--brand-yellow);
  }
  .tagline {
    position: absolute;
    top: 215px;
    left: 0;
    right: 0;
    text-align: center;
    font-weight: 600;
    font-size: 27px;
    letter-spacing: 0.5px;
    line-height: 1.3;
  }
  .product-name {
    position: absolute;
    top: 370px;
    left: 0;
    right: 0;
    text-align: center;
    font-weight: 800;
    font-size: 100px;
    line-height: 1;
    color: var(--brand-yellow);
  }
  .product-type {
    position: absolute;
    top: 488px;
    left: 0;
    right: 0;
    text-align: center;
    font-weight: 500;
    font-size: 30px;
  }
  .safety-claims {
    position: absolute;
    top: 600px;
    left: 40px;
    list-style: none;
    font-weight: 500;
    font-size: 22px;
    line-height: 1.45;
    color: var(--text-soft);
    text-transform: uppercase;
  }
  .suitability {
    position: absolute;
    right: 40px;
    bottom: 40px;
    text-align: right;
    font-weight: 500;
    font-size: 22px;
    line-height: 1.45;
    color: var(--text-soft);
  }
  .suitability ul { list-style: none; }
</style>
</head>
<body>
<main class="canvas">
  <section class="label">
    <div class="accent-area" role="img" aria-label="Decorative yellow accent graphic"></div>

    <h1 class="brand-name">DOVVRANTI</h1>
    <p class="tagline">PROFESSIONAL CLEANING<br>MAXIMUM PERFORMANCE</p>

    <h2 class="product-name">INK VANTI</h2>
    <p class="product-type">Advanced Anilox Cleaning Gel</p>

    <ul class="safety-claims">
      <li>Non Caustic</li>
      <li>Non Toxic</li>
      <li>Non Flammable</li>
      <li>Non Corrosive</li>
    </ul>

    <div class="suitability">
      <p>Suitable for:</p>
      <ul>
        <li>UV Based Inks</li>
        <li>Solvent-Based Inks</li>
        <li>Water-Based Inks</li>
      </ul>
    </div>
  </section>
</main>
</body>
</html>
```